Corvello Grey Horse Truck Design

Create a design to decorate a horse truck.
My Daughter does Dressage. Her horse is called 'Corvello Grey'. Corvello is a pure breed Lusitanian Stallion. We are based in the South of France and attend competitions all over the country. The truck made by Brantham which is a premium UK coach builder. The truck is being resprayed in 'Kestra Brisk Teal'. We would like a design that can be applied (painted) to the front, back and sides of the truck.
Attached are some photos of the truck, a car that is painted in Kestra Brisk Teal along with Corvello with my Daughter.
We would like something modern that will make the already distinctive colour even more memorable.

Target Market(s)

Equestrian

Requirements
Must have
• Clear graphic to decorate and already very distinctive truck
Should not have
• Too much text

```html
<!DOCTYPE html>
<html lang="en">
<head>
<meta charset="utf-8">
<title>Corvello Grey – Horse Truck Livery</title>
<link rel="stylesheet" href="https://fonts.googleapis.com/css2?family=Comfortaa:wght@500&family=Nunito+Sans:wght@300&display=swap">
<style>
  :root {
    --page: #ffffff;
    --navy: #00266b;
    --gold: #b98a00;
    --gold-soft: #a37b0c;
    --label: #ffffff;
  }
  * { box-sizing: border-box; margin: 0; padding: 0; }
  html, body {
    width: 1200px;
    height: 719px;
    overflow: hidden;
    background: var(--page);
  }
  .livery-sheet {
    position: relative;
    width: 1200px;
    height: 719px;
  }
  .truck-side {
    position: absolute;
    background: var(--navy);
    overflow: hidden;
  }
  .truck-side--front { left: 60px;  top: 57px;  width: 245px; height: 284px; }
  .truck-side--right { left: 340px; top: 57px;  width: 798px; height: 284px; }
  .truck-side--back  { left: 60px;  top: 376px; width: 245px; height: 285px; }
  .truck-side--left  { left: 340px; top: 376px; width: 798px; height: 285px; }

  .side-label {
    position: absolute;
    left: 5px;
    top: 3px;
    font-family: "Nunito Sans", sans-serif;
    font-weight: 300;
    font-size: 14.5px;
    line-height: 1;
    color: var(--label);
  }

  .horse-emblem {
    position: absolute;
    background: linear-gradient(160deg, var(--gold) 0%, var(--gold-soft) 100%);
    clip-path: polygon(0 0, 100% 0, 50% 100%);
  }
  .truck-side--front .horse-emblem { left: 138px; top: 33px; width: 69px;  height: 60px; }
  .truck-side--right .horse-emblem { left: 134px; top: 36px; width: 259px; height: 225px; }
  .truck-side--back  .horse-emblem { left: 122px; top: 128px; width: 106px; height: 91px; }
  .truck-side--left  .horse-emblem { left: 389px; top: 50px; width: 210px; height: 182px; }

  .horse-name {
    position: absolute;
    font-family: "Comfortaa", sans-serif;
    font-weight: 500;
    color: var(--gold);
    line-height: 1;
    white-space: nowrap;
    letter-spacing: -0.5px;
  }
  .truck-side--right .horse-name { left: 399px; top: 188px; font-size: 36px; }
  .truck-side--left  .horse-name { left: 185px; top: 188px; font-size: 36px; }
  .truck-side--back  .horse-name { left: 22px;  top: 205px; font-size: 16px; letter-spacing: -0.2px; }

  .gold-rule {
    position: absolute;
    height: 2px;
    background: var(--gold);
  }
  .truck-side--right .gold-rule { left: 379px; top: 222px; width: 419px; }
  .truck-side--left  .gold-rule { left: 0;     top: 223px; width: 418px; }

  .edge-mark {
    position: absolute;
    right: 0;
    top: 69px;
    width: 2px;
    height: 51px;
    background: var(--gold);
  }
</style>
</head>
<body>
<main class="livery-sheet">
  <section class="truck-side truck-side--front">
    <span class="side-label">front</span>
    <div class="horse-emblem" role="img" aria-label="Gold horse emblem artwork"></div>
  </section>

  <section class="truck-side truck-side--right">
    <span class="side-label">right</span>
    <div class="horse-emblem" role="img" aria-label="Large gold horse emblem artwork"></div>
    <p class="horse-name">Corvello Grey</p>
    <div class="gold-rule"></div>
  </section>

  <section class="truck-side truck-side--back">
    <span class="side-label">back</span>
    <div class="horse-emblem" role="img" aria-label="Gold horse emblem artwork"></div>
    <p class="horse-name">Corvello Grey</p>
    <div class="edge-mark"></div>
  </section>

  <section class="truck-side truck-side--left">
    <span class="side-label">left</span>
    <div class="horse-emblem" role="img" aria-label="Large gold horse emblem artwork, horse facing left"></div>
    <p class="horse-name">Corvello Grey</p>
    <div class="gold-rule"></div>
  </section>
</main>
</body>
</html>
```